Business Card Design

Dune Tanning Studio is a upmarket privately owned tanning and beauty salon. my card must look stylish. please also add appointment on back and facebook and instagram logos.

Industry/Entity Type

Business

Contact Information for Business Card

Dune Tanning Studio Pty Ltd
Solariums, Spray Tanning, Waxing & Eyelash Extensions
Shop 7-218 Carrow Bend Rd, Carrow Bend 4390
47619254

```html
<!DOCTYPE html>
<html lang="en">
<head>
<meta charset="utf-8">
<title>Dune Tanning Studio – Business Card</title>
<link href="https://fonts.googleapis.com/css2?family=Open+Sans:wght@400;600&family=Great+Vibes&display=swap" rel="stylesheet">
<style>
  :root {
    --stage: #8e8e8e;
    --card-black: #0c0c0c;
    --card-white: #ffffff;
    --ink-white: #f4f4f4;
    --teal: #2a94a0;
    --teal-soft: rgba(169, 214, 220, 0.8);
    --silver-soft: rgba(216, 216, 216, 0.45);
  }
  * { margin: 0; padding: 0; box-sizing: border-box; }
  html, body { width: 1200px; height: 900px; overflow: hidden; }
  body {
    background: var(--stage);
    font-family: "Open Sans", Arial, sans-serif;
    position: relative;
  }
  .card {
    position: absolute;
    width: 560px;
    height: 320px;
    border-radius: 16px;
    overflow: hidden;
    box-shadow: 0 10px 30px rgba(0,0,0,0.35);
  }

  /* Front */
  .card-front { left: 60px; top: 110px; background: var(--card-black); color: var(--ink-white); }
  .front-decor {
    position: absolute; inset: 0;
    background: radial-gradient(circle at 100% 50%, var(--silver-soft) 0%, rgba(216,216,216,0.2) 20%, rgba(216,216,216,0) 32%);
  }
  .front-company { position: absolute; left: 28px; top: 26px; font-size: 13px; line-height: 21px; letter-spacing: 0.3px; text-transform: uppercase; }
  .front-name { position: absolute; left: 40px; top: 78px; font-family: "Great Vibes", cursive; font-size: 46px; line-height: 56px; }
  .front-contact { position: absolute; left: 28px; top: 150px; font-size: 13px; line-height: 21px; }
  .front-services { position: absolute; left: 30px; top: 204px; list-style: none; font-size: 13px; line-height: 21px; }
  .front-services li::before { content: ""; display: inline-block; width: 6px; height: 6px; border-radius: 50%; background: var(--ink-white); margin-right: 12px; vertical-align: middle; }
  .front-brand { position: absolute; left: 300px; top: 140px; display: flex; align-items: center; gap: 10px; }
  .brand-dot { width: 14px; height: 14px; border-radius: 50%; background: var(--teal); }
  .brand-name { font-size: 20px; font-weight: 400; color: var(--teal); }

  /* Back */
  .card-back { left: 580px; top: 500px; background: var(--card-white); }
  .back-decor {
    position: absolute; inset: 0;
    background: radial-gradient(circle at 105% -10%, rgba(169,214,220,0) 52%, var(--teal-soft) 60%, var(--teal-soft) 68%, rgba(169,214,220,0) 80%);
  }
  .back-brand { position: absolute; left: 250px; top: 110px; display: flex; align-items: center; gap: 10px; }
  .back-follow { position: absolute; left: 330px; top: 178px; display: flex; align-items: center; gap: 8px; font-family: "Great Vibes", cursive; font-size: 20px; color: var(--teal); }
  .social-square { width: 26px; height: 26px; border-radius: 5px; background: var(--teal); }
  .back-appointment { position: absolute; left: 120px; top: 258px; width: 400px; display: flex; align-items: flex-end; gap: 6px; font-family: "Great Vibes", cursive; font-size: 20px; color: var(--teal); }
  .appointment-line { flex: 1; height: 1px; background: var(--teal); margin-bottom: 5px; }
</style>
</head>
<body>
  <section class="card card-front" aria-label="Card front">
    <div class="front-decor" role="img" aria-label="Silver dot pattern decoration"></div>
    <p class="front-company">Dune Tanning Studio Pty Ltd<br>Shop 7-218 Carrow Bend Rd, Carrow Bend</p>
    <p class="front-name">mara ellis</p>
    <p class="front-contact">Phone:&nbsp; 4390 4761 9254<br>E-mail:&nbsp; maraellis@dunetanning.com</p>
    <ul class="front-services">
      <li>Solariums</li>
      <li>Spray Tanning</li>
      <li>Waxing</li>
      <li>Eyelash Extensions</li>
    </ul>
    <div class="front-brand">
      <span class="brand-dot"></span>
      <span class="brand-name">Dune Tanning Studio</span>
    </div>
  </section>

  <section class="card card-back" aria-label="Card back">
    <div class="back-decor" role="img" aria-label="Soft teal dot pattern decoration"></div>
    <div class="back-brand">
      <span class="brand-dot"></span>
      <span class="brand-name">Dune Tanning Studio</span>
    </div>
    <div class="back-follow">
      <span>Follow me in:</span>
      <span class="social-square"></span>
      <span class="social-square"></span>
    </div>
    <div class="back-appointment">
      <span>Appointment:</span>
      <span class="appointment-line"></span>
    </div>
  </section>
</body>
</html>
```